body balm label design

body balm tube design, current label design for other similar products
Need to have a design which can interchange between 3 different solutions
Quiet Orchard (Lavender + Vanilla)
Copper Trail (Eucalyptus + Mint)
Fern Hollow (Bergamot + Cedarwood)
Tube size:
2.5h x 3.25 w
Target Market(s)
natural, solution focused
Requirements
Must have
- relatable to existing brand designs, focus on features and benefits

```html
<!DOCTYPE html>
<html lang="en">
<head>
<meta charset="utf-8">
<title>Quiet Orchard Body Balm Label</title>
<link href="https://fonts.googleapis.com/css2?family=Playfair+Display:wght@500&family=Montserrat:wght@400;500&family=Libre+Caslon+Text&family=Allura&display=swap" rel="stylesheet">
<style>
  :root {
    --backdrop: #bccfcf;
    --label: #ffffff;
    --panel: #5f8a86;
    --panel-dark: #4d7773;
    --ink: #3f6f6b;
    --ink-soft: #6f8f8c;
    --on-panel: #e9f1f0;
  }
  * { margin: 0; padding: 0; box-sizing: border-box; }
  html, body { width: 1200px; height: 1001px; overflow: hidden; }
  body {
    background: var(--backdrop);
    position: relative;
    font-family: "Libre Caslon Text", serif;
  }
  .label {
    position: absolute;
    top: 180px;
    width: 420px;
    height: 640px;
    background: var(--label);
    border-radius: 6px;
    overflow: hidden;
  }
  .label--front { left: 150px; }
  .label--back { left: 630px; }

  /* front */
  .panel {
    position: absolute;
    left: 0; top: 70px;
    width: 236px; height: 520px;
    background: linear-gradient(180deg, var(--panel) 0%, var(--panel-dark) 100%);
    border-top-left-radius: 110px;
    color: var(--on-panel);
  }
  .panel__type {
    position: absolute;
    top: 78px; left: 0; right: 0;
    text-align: center;
    font-family: "Montserrat", sans-serif;
    font-size: 15px;
    letter-spacing: 3px;
    line-height: 26px;
  }
  .panel__rule {
    position: absolute;
    left: 60px; right: 50px;
    height: 1px;
    background: var(--on-panel);
    opacity: .7;
  }
  .panel__rule--top { top: 140px; }
  .panel__rule--bottom { top: 168px; }
  .panel__scent {
    position: absolute;
    top: 147px; left: 0; right: 0;
    text-align: center;
    font-size: 9px;
    letter-spacing: 1px;
  }
  .panel__seal {
    position: absolute;
    top: 186px; left: 22px;
    width: 66px; height: 66px;
    border-radius: 50%;
    border: 1px solid rgba(233,241,240,.6);
    display: flex; flex-direction: column; align-items: center; justify-content: center;
    font-size: 7px; line-height: 10px; letter-spacing: .5px; text-align: center;
  }
  .panel__seal strong { font-size: 10px; font-weight: 400; }
  .panel__art {
    position: absolute;
    left: 40px; top: 200px;
    width: 150px; height: 310px;
    border-radius: 70px 70px 8px 8px;
    background: linear-gradient(180deg, rgba(233,241,240,.16), rgba(233,241,240,.06));
  }
  .title {
    position: absolute;
    left: 244px; top: 70px;
    height: 520px;
    writing-mode: vertical-rl;
    transform: rotate(180deg);
    font-family: "Playfair Display", serif;
    font-weight: 500;
    font-size: 57px;
    line-height: 1;
    color: var(--ink);
    letter-spacing: 1px;
    text-align: center;
    white-space: nowrap;
  }
  .net-weight {
    position: absolute;
    left: 0; top: 604px;
    width: 236px;
    text-align: center;
    font-family: "Montserrat", sans-serif;
    font-weight: 500;
    font-size: 13px;
    color: var(--ink);
  }

  /* back */
  .back__content {
    position: absolute;
    left: -60px; top: 130px;
    width: 540px; height: 380px;
    transform: rotate(-90deg);
    padding: 18px 20px;
    color: var(--ink-soft);
  }
  .claims {
    display: flex; align-items: center; gap: 14px;
    font-family: "Allura", cursive;
    font-size: 30px;
    color: var(--ink);
    white-space: nowrap;
  }
  .claims__line { flex: 1; height: 1px; background: var(--ink-soft); opacity: .6; }
  .ingredients__head {
    margin-top: 18px;
    text-align: center;
    font-size: 12px;
  }
  .ingredients {
    margin-top: 6px;
    font-size: 11.5px;
    line-height: 22px;
    text-align: center;
  }
  .back__rule { margin: 14px 0 10px; height: 1px; background: var(--ink-soft); opacity: .5; }
  .maker {
    display: flex; align-items: center; gap: 22px;
    font-size: 8px; letter-spacing: .6px;
  }
  .maker__social { margin-left: auto; display: flex; gap: 10px; }
  .maker__dot { width: 15px; height: 15px; border-radius: 50%; background: var(--ink-soft); }
</style>
</head>
<body>
  <section class="label label--front">
    <div class="panel">
      <p class="panel__type">BODY<br>BALM</p>
      <span class="panel__rule panel__rule--top"></span>
      <p class="panel__scent">LAVENDER + VANILLA</p>
      <span class="panel__rule panel__rule--bottom"></span>
      <div class="panel__art" role="img" aria-label="Fine line drawing of lavender sprigs"></div>
      <div class="panel__seal"><span>MADE IN</span><strong>100%</strong><span>NATURAL</span><span>CANADA</span></div>
    </div>
    <h1 class="title">QUIET ORCHARD</h1>
    <p class="net-weight">Net Wt. 0.5oz / 14 g</p>
  </section>

  <section class="label label--back">
    <div class="back__content">
      <div class="claims">
        <span>plant based</span><span class="claims__line"></span>
        <span>vegan</span><span class="claims__line"></span>
        <span>cruelty free</span>
      </div>
      <p class="ingredients__head">Ingredients:</p>
      <p class="ingredients">Organic Olive Fruit Oil (Olea Europaea), Organic Coconut Oil (Cocos Nucifera), Organic Shea Butter (Butyrospermum Parkii), Organic Jojoba Seed Oil (Simmondsia Chinensis), Rosehip Seed Oil (Rosa Canina), Vitamin E (Tocopherol), Sunflower Seed Oil (Helianthus Annuus), Vanilla Aroma, Mentha Piperita (Peppermint) Leaf Oil, Dipteryx Odorata (Tonka Bean) Oil</p>
      <div class="back__rule"></div>
      <div class="maker">
        <span>WWW.WILLOWFERN.CA</span>
        <span>Made by Willow Fern Co., Millbrook, AB T0L 2B4</span>
        <span class="maker__social"><span class="maker__dot"></span><span class="maker__dot"></span><span class="maker__dot"></span></span>
      </div>
    </div>
  </section>
</body>
</html>
```